Redesign Colorful Business Card

Please redesign the card attached. It is too busy. Please don't eliminate any of the words. The repetivite word "free" can be used less often.

Target Market(s)

College Students.

Contact Information for Business Card

The details listed in the attached image

Font styles to use
Sans Serif

Requirements
Must have
• A clear and simple presentation and must be attractive.

```html
<!DOCTYPE html>
<html lang="en">
<head>
<meta charset="utf-8">
<title>StudyNimbl Business Card</title>
<link rel="stylesheet" href="https://fonts.googleapis.com/css2?family=Oswald:wght@400;500&family=Arimo:wght@400;700&display=swap">
<style>
  :root {
    --page-bg: #cbcbcb;
    --card-red: #ff1a10;
    --card-coral: #fb7f5c;
    --card-cream: #f5e3a0;
    --badge-yellow: #f7cd17;
    --badge-text: #1d1d1d;
    --forest: #07432f;
    --mist: #eaf3f0;
    --royal: #2236f0;
    --white: #ffffff;
    --ink: #1a1a1a;
  }
  * { box-sizing: border-box; margin: 0; padding: 0; }
  html, body {
    width: 1200px;
    height: 875px;
    overflow: hidden;
    background: var(--page-bg);
  }
  .business-card {
    position: absolute;
    left: 230px;
    top: 218px;
    width: 738px;
    height: 438px;
    background: linear-gradient(35deg, var(--card-red) 10%, var(--card-coral) 48%, var(--card-cream) 100%);
    overflow: hidden;
  }
  .brand {
    position: absolute;
    left: 27px;
    top: 160px;
    display: flex;
    align-items: center;
    gap: 14px;
  }
  .brand-dot {
    width: 46px;
    height: 46px;
    border-radius: 50%;
    background: var(--badge-yellow);
  }
  .brand-name {
    font-family: "Oswald", "Arial Narrow", sans-serif;
    font-weight: 500;
    font-size: 44px;
    line-height: 1;
    color: var(--white);
  }
  .site-address {
    position: absolute;
    left: 25px;
    top: 350px;
    font-family: "Arimo", Arial, sans-serif;
    font-size: 26px;
    color: var(--white);
  }
  .free-badge {
    position: absolute;
    left: 341px;
    top: 40px;
    height: 36px;
    padding: 0 22px;
    border-radius: 18px;
    background: var(--badge-yellow);
    color: var(--badge-text);
    font-family: "Arimo", Arial, sans-serif;
    font-weight: 700;
    font-size: 16px;
    letter-spacing: 1px;
    display: flex;
    align-items: center;
  }
  .benefit {
    position: absolute;
    left: 341px;
    width: 345px;
    height: 85px;
    border-radius: 10px;
    padding: 0 20px 0 29px;
    display: flex;
    align-items: center;
    font-family: "Oswald", "Arial Narrow", sans-serif;
    font-size: 27px;
    line-height: 1.15;
  }
  .benefit--time { top: 91px; background: var(--forest); color: var(--white); }
  .benefit--class { top: 186px; background: var(--mist); color: var(--forest); }
  .benefit--memory { top: 282px; background: var(--royal); color: var(--white); }
  .copyright {
    position: absolute;
    right: 56px;
    top: 400px;
    font-family: "Arimo", Arial, sans-serif;
    font-size: 16px;
    color: var(--ink);
  }
</style>
</head>
<body>
  <main class="business-card">
    <div class="brand">
      <span class="brand-dot"></span>
      <span class="brand-name">StudyNimbl</span>
    </div>
    <p class="site-address">StudyNimbl.com</p>

    <span class="free-badge">FREE</span>
    <p class="benefit benefit--time">Cut Study Time down by<br>up to 50%</p>
    <p class="benefit benefit--class">Learn a subject without<br>having to go to class</p>
    <p class="benefit benefit--memory">Memorize anything quickly</p>

    <p class="copyright">Copyright Nimbl Services, LLc 2013-2022 All Rights Reserved</p>
  </main>
</body>
</html>
```